Corvane Bookkeeping Services business cards

looking for a double sided business card design. My logo is attached. I am looking for a design similar to the attached. Keen to see what my logo in white on the blue background would look like.

```html
<!DOCTYPE html>
<html lang="en">
<head>
<meta charset="utf-8">
<title>Corvane Bookkeeping Services – Business Cards</title>
<link rel="stylesheet" href="https://fonts.googleapis.com/css2?family=Montserrat:wght@400;500;700;800&display=swap">
<style>
  :root {
    --canvas: #dfe0e2;
    --navy: #1e3a6b;
    --white: #ffffff;
    --mark-faint: #e3e4e6;
    --icon: #5a5f66;
  }
  * { margin: 0; padding: 0; box-sizing: border-box; }
  html, body {
    width: 1200px;
    height: 1200px;
    overflow: hidden;
    background: var(--canvas);
    font-family: "Montserrat", Arial, sans-serif;
  }
  .card {
    position: absolute;
    width: 855px;
    height: 466px;
    border-radius: 36px;
  }
  .card-front {
    left: 168px;
    top: 94px;
    background: var(--navy);
  }
  .card-back {
    left: 163px;
    top: 632px;
    background: var(--white);
    color: var(--navy);
  }

  /* Wordmark */
  .wordmark {
    position: absolute;
    font-weight: 800;
    line-height: 1;
  }
  .wordmark .wordmark-name { display: block; letter-spacing: -0.5px; }
  .wordmark .wordmark-tagline { display: block; text-transform: uppercase; letter-spacing: 1px; }

  .card-front .wordmark {
    left: 0;
    right: 0;
    top: 178px;
    display: flex;
    justify-content: center;
    align-items: center;
    gap: 22px;
    color: var(--white);
  }
  .card-front .wordmark-square {
    width: 96px;
    height: 96px;
    background: var(--white);
  }
  .card-front .wordmark-name { font-size: 84px; }
  .card-front .wordmark-tagline { font-size: 23px; margin-top: 6px; }

  .card-back .wordmark {
    left: 63px;
    top: 62px;
    color: var(--navy);
  }
  .card-back .wordmark-name { font-size: 50px; }
  .card-back .wordmark-tagline { font-size: 14.5px; margin-top: 3px; letter-spacing: 0.6px; }

  .faint-mark {
    position: absolute;
    left: 600px;
    top: 70px;
    width: 210px;
    height: 210px;
    background: var(--mark-faint);
  }

  .person {
    position: absolute;
    left: 63px;
    top: 176px;
  }
  .person-name { font-size: 26px; font-weight: 500; letter-spacing: 0.3px; }
  .person-role { font-size: 19px; font-weight: 500; margin-top: 8px; margin-left: 2px; }

  .contact-list {
    position: absolute;
    left: 68px;
    top: 274px;
    list-style: none;
  }
  .contact-list li {
    display: flex;
    align-items: center;
    gap: 12px;
    height: 37px;
    font-size: 20px;
    font-weight: 500;
  }
  .contact-list svg { width: 16px; height: 16px; fill: var(--icon); flex: none; }

  .address {
    position: absolute;
    right: 62px;
    top: 350px;
    text-align: right;
    font-size: 20px;
    font-weight: 500;
    line-height: 36px;
    font-style: normal;
  }
</style>
</head>
<body>

<section class="card card-front" aria-label="Card front">
  <div class="wordmark">
    <span class="wordmark-square" aria-hidden="true"></span>
    <div>
      <span class="wordmark-name">Corvane</span>
      <span class="wordmark-tagline">Bookkeeping Services</span>
    </div>
  </div>
</section>

<section class="card card-back" aria-label="Card back">
  <div class="wordmark">
    <span class="wordmark-name">Corvane</span>
    <span class="wordmark-tagline">Bookkeeping Services</span>
  </div>

  <div class="faint-mark" aria-hidden="true"></div>

  <div class="person">
    <p class="person-name">YOUR NAME</p>
    <p class="person-role">Director</p>
  </div>

  <ul class="contact-list">
    <li>
      <svg viewBox="0 0 16 16" aria-hidden="true"><path d="M1 5c0-2 2-3 7-3s7 1 7 3v1h-4V5H5v1H1zM4 7h8l2 3v4H2v-4zm4 2a2 2 0 1 0 0 4a2 2 0 1 0 0-4z"/></svg>
      (123) 444-5555
    </li>
    <li>
      <svg viewBox="0 0 16 16" aria-hidden="true"><path d="M4 1h8v4H4zM1 6h14v6h-3v3H4v-3H1zm4 4v3h6v-3z"/></svg>
      (123) 444-5556
    </li>
    <li>
      <svg viewBox="0 0 16 16" aria-hidden="true"><path d="M1 3h14v1L8 9 1 4zm0 3l7 5 7-5v7H1z"/></svg>
      urmail@yoursite.com
    </li>
    <li>
      <svg viewBox="0 0 16 16" aria-hidden="true"><path d="M8 1a7 7 0 1 0 0 14A7 7 0 1 0 8 1zm0 1.5c.9 1 1.5 2.6 1.6 4.7H6.4C6.5 5.1 7.1 3.5 8 2.5zM5 7.2H2.6A5.5 5.5 0 0 1 5.6 3 9 9 0 0 0 5 7.2zm0 1.6a9 9 0 0 0 .6 4.2 5.5 5.5 0 0 1-3-4.2zm1.4 0h3.2c-.1 2.1-.7 3.7-1.6 4.7-.9-1-1.5-2.6-1.6-4.7zm4.6 0h2.4a5.5 5.5 0 0 1-3 4.2 9 9 0 0 0 .6-4.2zm0-1.6a9 9 0 0 0-.6-4.2 5.5 5.5 0 0 1 3 4.2z"/></svg>
      www.yoursite.com
    </li>
  </ul>

  <address class="address">
    1234 Your Address<br>
    Country Name, AA 1234
  </address>
</section>

</body>
</html>
```